Cover of the e-book award-winning national sports figure.

I would like to utilize the picture this attached to this brief. If you could pull the trophies and myself out and place with the new background, that’s what I would like to see . I would like to have a new bookcover design for my e-book. I attached below the original cover and have marked in red. The things that I don’t want on the new cover. I’ve attached a picture that’s not the original. I’m waiting on the high copy. I would like to replace the old logo with the one that I have attached. The website that I would like to have on the book is www.dellanvmoreaux.com.
Target Market(s)
Biography
Industry/Entity Type
Sports & motivation?
Requirements
Must have
- Picture of me in the blue suit on the cover the title of the book walking past midnight lessons from quiet harbors
Nice to have
- Utilize the old cover that I have attached for some ideas
Should not have
- The cover should not have anything related to marlow crest press Inc.

```html
<!DOCTYPE html>
<html lang="en">
<head>
<meta charset="utf-8">
<title>Walking Past Midnight — Book Cover</title>
<link href="https://fonts.googleapis.com/css2?family=Lato:ital,wght@0,400;0,700;0,900;1,400;1,700&family=Oswald:wght@400;500&family=Playfair+Display:wght@400;500&display=swap" rel="stylesheet">
<style>
  :root{
    --page-light:#e6eff8;
    --slate:#5f6b78;
    --navy:#1b2d57;
    --ink:#17284a;
    --accent-blue:#1a7acc;
    --title-blue:#c5d9ee;
    --band-blue:#7ba8d8;
    --white:#ffffff;
  }
  *{margin:0;padding:0;box-sizing:border-box}
  html,body{width:1200px;height:871px;overflow:hidden;background:var(--page-light)}
  .cover{position:relative;width:1200px;height:871px;overflow:hidden;background:var(--page-light);font-family:"Lato",sans-serif}
  .abs{position:absolute}

  /* back cover */
  .rule{background:var(--accent-blue);height:9px}
  .rule--top{left:0;top:33px;width:505px}
  .rule--bottom{left:0;top:720px;width:440px;height:8px}
  .blurb{left:47px;top:60px;width:346px;color:var(--ink);font-size:15.2px;line-height:18.8px}
  .blurb strong.lead{font-weight:700;font-size:20px;line-height:20.6px}
  .blurb em{font-weight:700;font-style:italic}
  .blurb p+p{margin-top:18px}
  .back-photo{left:398px;top:35px;width:172px;height:700px;border-radius:80px 80px 20px 20px;background:linear-gradient(180deg,#b98b6a 0%,#f2e49a 25%,#e8dc95 40%,#2a2a2e 55%,#1f1f23 85%,#f4f4f4 100%)}
  .mark{display:flex;align-items:center;gap:6px;color:var(--ink);font-weight:700;font-size:10px;letter-spacing:.3px;text-transform:uppercase;white-space:nowrap}
  .mark__dot{width:22px;height:22px;border-radius:50%;background:var(--accent-blue);flex:none}
  .mark--back{left:52px;top:748px}
  .visit{left:47px;top:804px;font-size:15.5px;color:var(--ink)}
  .code-box{left:270px;top:728px;width:189px;height:92px;background:var(--white);border-radius:6px}

  /* slate panel and spine */
  .slate{left:505px;top:0;width:616px;height:665px;background:var(--slate)}
  .spine-line{top:0;width:2px;height:871px;background:rgba(255,255,255,.18)}
  .spine-title{left:576px;top:34px;width:48px;height:230px;display:flex;align-items:center;justify-content:center}
  .spine-title span{transform:rotate(90deg);white-space:nowrap;font-family:"Playfair Display",serif;font-size:25px;color:var(--accent-blue)}
  .spine-title small{font-family:"Oswald",sans-serif;font-size:14px}
  .spine-name{left:576px;top:690px;width:48px;height:140px;display:flex;align-items:center;justify-content:center}
  .spine-name span{transform:rotate(90deg);white-space:nowrap;font-family:"Lato",sans-serif;font-weight:700;font-size:30px;color:var(--accent-blue)}

  /* front cover */
  .author-band{left:730px;top:0;width:470px;height:88px;background:var(--navy);color:var(--white);font-weight:700;font-size:38px;display:flex;align-items:center;padding-left:56px;white-space:nowrap}
  .title{left:645px;top:96px;width:410px;color:var(--title-blue);font-family:"Playfair Display",serif;font-weight:400;line-height:1}
  .title__big{display:block;font-size:80px;letter-spacing:-1.5px}
  .title__big--second{font-size:70px}
  .title__row{display:flex;align-items:flex-end;gap:10px;margin-top:2px}
  .title__small{font-family:"Oswald",sans-serif;font-size:30px;color:var(--title-blue);border-bottom:3px solid var(--title-blue);padding-bottom:3px;margin-bottom:12px}
  .subtitle{left:637px;top:316px;width:319px;height:37px;background:var(--band-blue);color:var(--navy);font-style:italic;font-size:23px;display:flex;align-items:center;padding-left:20px;white-space:nowrap}
  .foreword{left:736px;top:358px;color:var(--white);font-family:"Oswald",sans-serif;font-size:18px;letter-spacing:-.3px;white-space:nowrap}
  .foreword b{font-weight:400;font-size:28px}
  .intro{left:657px;top:416px;width:315px;color:var(--white);font-style:italic;font-size:10.3px;line-height:14.3px}
  .intro p+p{margin-top:14px;width:148px}
  .mark--front{left:665px;top:720px;color:var(--ink)}
  .site-box{left:637px;top:782px;width:172px;height:39px;background:var(--slate);color:var(--white);font-family:"Playfair Display",serif;font-size:15px;display:flex;align-items:center;padding-left:14px;white-space:nowrap;z-index:2}
  .trophies{left:810px;top:505px;width:190px;height:366px;border-radius:60px 60px 4px 4px;background:linear-gradient(180deg,#dfe4ea 0%,#aab3bd 40%,#8e969f 70%,#3b2a22 100%)}
  .front-photo{left:985px;top:130px;width:215px;height:741px;background:linear-gradient(180deg,#8a5c45 0%,#7a4f3b 18%,#e9eef4 26%,#2a47a0 35%,#233e8f 100%);clip-path:polygon(78px 0,190px 0,215px 60px,215px 100%,0 100%,0 210px,30px 175px,78px 160px)}
</style>
</head>
<body>
<div class="cover">
  <!-- back cover -->
  <div class="abs rule rule--top"></div>
  <div class="abs back-photo" role="img" aria-label="Full-length photo of the author in a yellow shirt holding two silver championship trophies"></div>
  <div class="abs blurb">
    <p><strong class="lead">As the starting fullback for the Harbor City Gulls, Dellan V. Moreaux leads the way for tailback Marcus Ellery and has gained a reputation as the consummate team player.</strong> He played a central role in the two League Title championship victories garnered by the Gulls in ’97 and ’98. Now, in <em>Walking Past Midnight</em>, Moreaux defines what it means to be a team player. He uses football as a metaphor for life - how to make the most of your talent, master your inhibitions, and overcome personal limitations. Moreaux provides strategies that enhance individual performance and translate into team success. From the boardroom to the Little League field, <em>Walking Past Midnight</em> is for those with a burning desire to succeed. Moreaux shares his stories of victory and personal defeat, struggles, and triumphs. Through his experiences as a pro league player, you learn the importance of developing and executing a game plan that puts you and your team at the top of your game.</p>
    <p>Dellan V. Moreaux is the recipient of the “Unsung Hero” Award (1998). He frequently makes special appearances for various charities and lends financial support to the Riverton Public Schools’ football program. In the off-season, he conducts speaking engagements for corporations, schools, and other social organizations. He lives in Colorado with his wife, Renata, and their two sons.</p>
  </div>
  <div class="abs rule rule--bottom"></div>
  <div class="abs mark mark--back"><span class="mark__dot"></span>Dellan V. Moreaux</div>
  <div class="abs code-box"></div>
  <div class="abs visit">Visit www.dellanvmoreaux.com.</div>

  <!-- slate panel and spine -->
  <div class="abs slate"></div>
  <div class="abs spine-line" style="left:575px"></div>
  <div class="abs spine-line" style="left:623px"></div>
  <div class="abs spine-title"><span>Walking <small>PAST</small> Midnight</span></div>
  <div class="abs spine-name"><span>Moreaux</span></div>

  <!-- front cover -->
  <div class="abs author-band">Dellan V. Moreaux</div>
  <h1 class="abs title">
    <span class="title__big">Walking</span>
    <span class="title__row"><span class="title__small">PAST</span><span class="title__big title__big--second">Midnight</span></span>
  </h1>
  <div class="abs subtitle">Lessons from Quiet Harbors</div>
  <div class="abs foreword">Foreword by <b>Marcus Ellery</b></div>
  <div class="abs intro">
    <p>Becoming a team player is absolutely crucial to your ultimate success. Learning to play within the framework of a team atmosphere not only strengthens your individual ability, but it also gives you a tremendous feeling of accomplishment knowing that you’ve been instrumental in moving an entire group of people a little closer to the collective dream.</p>
    <p>I believe that the personal and professional experiences shared in this book will offer strategies that can be used in any team situation, whether it’s a corporate sales force, a little league sports team, a social organization or a family unit.</p>
  </div>
  <div class="abs mark mark--front"><span class="mark__dot"></span>Dellan V. Moreaux</div>
  <div class="abs trophies" role="img" aria-label="Two silver championship trophies on a dark wooden stand"></div>
  <div class="abs site-box">dellanvmoreaux.com</div>
  <div class="abs front-photo" role="img" aria-label="Photo of the author smiling in a blue pinstripe suit with paisley tie"></div>
</div>
</body>
</html>
```